Propose a revamped landing page

One template we like eg is https://www.trovask.com but but cluttered Our logo and colors are attached to our logo and colors are printed on a white background what we have. So font usage ...
1 page

```html
<!DOCTYPE html>
<html lang="en">
<head>
<meta charset="utf-8">
<title>Sunvolt – Always switch to the cheapest energy provider</title>
<link href="https://fonts.googleapis.com/css2?family=Josefin+Sans:wght@300;400;600;700&display=swap" rel="stylesheet">
<style>
:root{
  --orange:#f7a91c;
  --orange-deep:#f29a0e;
  --orange-light:#ffc94a;
  --ink:#3b4148;
  --text:#4a4f55;
  --white:#ffffff;
  --night:#1f2a36;
  --footer:#3a3e44;
}
*{margin:0;padding:0;box-sizing:border-box}
html,body{width:1200px;height:2917px;overflow:hidden}
body{position:relative;background:var(--white);font-family:'Josefin Sans',Arial,sans-serif;color:var(--text)}
.abs{position:absolute}

/* header */
.site-header{position:absolute;left:0;top:0;width:1200px;height:101px;background:var(--white)}
.brand{position:absolute;left:88px;top:26px;display:flex;align-items:center;gap:10px;color:var(--orange);font-weight:700;font-size:40px;line-height:1}
.brand-dot{width:22px;height:22px;border-radius:50%;background:var(--ink)}
.main-nav{position:absolute;left:313px;top:44px;display:flex;gap:23px;font-size:14px;color:var(--ink)}
.btn{display:flex;align-items:center;justify-content:center;font-size:14px;color:var(--white)}
.btn-header{position:absolute;left:939px;top:27px;width:175px;height:47px;background:var(--orange)}

/* hero */
.hero{position:absolute;left:0;top:101px;width:1200px;height:512px;background:linear-gradient(90deg,var(--orange) 0%,var(--orange) 40%,var(--orange-light) 70%,var(--orange) 100%)}
.hero-art{position:absolute;left:480px;top:0;width:720px;height:512px;background:radial-gradient(circle at 355px 187px,#fffbe8 0%,#ffe27a 14%,rgba(255,196,60,.6) 38%,rgba(247,169,28,0) 70%)}
.hero-kicker{position:absolute;left:130px;top:141px;font-size:20px;font-weight:600;color:var(--white)}
.hero-title{position:absolute;left:130px;top:170px;font-size:52px;font-weight:400;color:var(--ink)}
.hero-rule{position:absolute;left:130px;top:237px;width:325px;height:1px;background:rgba(255,255,255,.8)}
.hero-sub{position:absolute;left:130px;top:254px;font-size:21px;line-height:28px;font-weight:600;color:var(--white);letter-spacing:.5px}
.btn-hero{position:absolute;left:130px;top:327px;width:175px;height:47px;background:var(--ink)}

/* intro */
.intro-title{position:absolute;left:0;top:698px;width:1200px;text-align:center;font-size:40px;line-height:52px;color:var(--orange)}
.intro-copy{position:absolute;left:300px;top:831px;width:600px;text-align:center;font-size:15px;line-height:20px;color:var(--ink)}
.intro-copy p{margin-bottom:20px}

/* banner */
.banner{position:absolute;left:0;top:1060px;width:1200px;height:401px;background:linear-gradient(90deg,var(--night) 0%,#2a3644 45%,#43413f 75%,#5a4438 100%)}
.banner-title{position:absolute;left:0;top:1083px;width:1200px;text-align:center;font-size:40px;line-height:54px;color:var(--white)}
.savings-art{position:absolute;left:400px;top:1340px;width:400px;height:210px;border-radius:105px;background:linear-gradient(180deg,#fbfbfb 0%,#2fb3a4 40%,#36a596 100%);box-shadow:0 12px 20px rgba(0,0,0,.2)}

/* features */
.section-title{position:absolute;left:0;width:1200px;text-align:center;font-size:40px;color:var(--ink)}
.features{position:absolute;left:0;top:1745px;width:1200px;height:335px;background:var(--orange)}
.feature{position:absolute;top:0;width:400px;height:335px;text-align:center;color:var(--white)}
.feature.raised{top:-4px;height:343px;background:var(--orange);box-shadow:0 8px 24px rgba(0,0,0,.22)}
.feature svg{position:absolute;left:170px;top:72px}
.feature h3{position:absolute;left:0;top:172px;width:400px;font-size:22px;font-weight:600;letter-spacing:.5px}
.feature p{position:absolute;left:90px;top:212px;width:220px;font-size:14px;line-height:21px;font-weight:300}

/* steps */
.step-photo{position:absolute;left:150px;top:2256px;width:342px;height:342px;border-radius:50%;border:8px solid #eef4f8;background:linear-gradient(135deg,#cfe4f3,#9cc4e0 60%,#e7eef3);box-shadow:0 4px 14px rgba(0,0,0,.12)}
.step-line{position:absolute;height:1px;background:var(--orange)}
.step-num{position:absolute;width:34px;height:34px;border-radius:50%;background:var(--orange);color:var(--white);font-size:17px;display:flex;align-items:center;justify-content:center;padding-top:3px}
.step-text{position:absolute;color:var(--ink)}
.step-text h4{font-size:20px;font-weight:600;margin-bottom:8px}
.step-text p{font-size:14px;line-height:21px}
.btn-cta{position:absolute;left:513px;top:2665px;width:175px;height:46px;background:var(--orange)}

/* footer */
.site-footer{position:absolute;left:0;top:2801px;width:1200px;height:116px;background:var(--footer)}
.footer-brand{position:absolute;left:88px;top:42px;font-size:34px;font-weight:700;color:var(--orange)}
.footer-nav{position:absolute;left:315px;top:52px;font-size:11px;color:var(--white);word-spacing:2px}
.copyright{position:absolute;left:817px;top:52px;font-size:11px;color:var(--white)}
.social{position:absolute;left:1100px;top:50px;width:18px;height:18px;border-radius:50%;background:var(--white)}
</style>
</head>
<body>

<header class="site-header">
  <div class="brand">Sunvolt<span class="brand-dot"></span></div>
  <nav class="main-nav">
    <span>That's How It Works</span><span>Prices</span><span>Ask?</span><span>About Us</span><span>Operations</span><span>Experience</span><span>Press</span>
  </nav>
  <div class="btn btn-header">Register Now</div>
</header>

<section class="hero">
  <div class="hero-art" role="img" aria-label="Glowing figure with outstretched arms in a burst of sunlight"></div>
  <div class="hero-kicker">Welcome to</div>
  <h1 class="hero-title">Sunvolt</h1>
  <div class="hero-rule"></div>
  <p class="hero-sub">Always automatically switch to<br>the cheapest energy provider.</p>
  <div class="btn btn-hero">Register Now</div>
</section>

<h2 class="intro-title">Never Pay too much for<br>Electricity &amp; Gas again</h2>
<div class="intro-copy">
  <p>Gone are the days of bad deals, tedious rate comparison and boring exchange forms.</p>
  <p>With the automatic change service for Sunvolt members you will never again pay too much for electricity and gas. And that, without touching a finger. We fight for you through the tariff jungle.</p>
  <p>So save your hard earned money and become a Sunvolt member.</p>
</div>

<section class="banner" role="img" aria-label="Solar panels on a tiled house roof at dusk"></section>
<h2 class="banner-title">The Cheapest of all<br>Super Powers</h2>
<div class="savings-art" role="img" aria-label="Cloud-shaped illustration of a small town with a savings badge of up to 850 euros"></div>

<h2 class="section-title" style="top:1660px">Register Once, Always Save</h2>
<section class="features">
  <div class="feature" style="left:0">
    <svg width="60" height="60" viewBox="0 0 60 60" fill="none" stroke="#fff" stroke-width="2" stroke-linejoin="round"><path d="M4 28 56 6 44 54 28 36Z"/><path d="M56 6 28 36 24 52 28 36"/></svg>
    <h3>Independently</h3>
    <p>We work only for you. In order to remain independent.</p>
  </div>
  <div class="feature raised" style="left:400px">
    <svg width="60" height="60" viewBox="0 0 60 60" fill="none" stroke="#fff" stroke-width="2"><circle cx="24" cy="24" r="7"/><circle cx="24" cy="24" r="15" stroke-dasharray="6 4"/><circle cx="44" cy="42" r="5"/><circle cx="44" cy="42" r="11" stroke-dasharray="5 3"/></svg>
    <h3>Automatically</h3>
    <p>You sign up once and we'll do the rest. All automatically.</p>
  </div>
  <div class="feature" style="left:800px">
    <svg width="60" height="60" viewBox="0 0 60 60" fill="none" stroke="#fff" stroke-width="2" stroke-linejoin="round"><path d="M14 18 36 6 42 18"/><rect x="6" y="18" width="48" height="34" rx="3"/><path d="M54 28H40a6 6 0 0 0 0 12h14"/><circle cx="41" cy="34" r="2"/></svg>
    <h3>Fair</h3>
    <p>Sunvolt members keep more in their wallet. Despite service charge.</p>
  </div>
</section>

<h2 class="section-title" style="top:2168px">How do I become Sunvolt?</h2>
<div class="step-photo" role="img" aria-label="Person pulling open a shirt to reveal an emblem underneath"></div>
<div class="step-line" style="left:340px;top:2313px;width:265px"></div>
<div class="step-line" style="left:410px;top:2446px;width:255px"></div>
<div class="step-line" style="left:350px;top:2577px;width:255px"></div>
<div class="step-num" style="left:588px;top:2280px">1</div>
<div class="step-num" style="left:648px;top:2413px">2</div>
<div class="step-num" style="left:588px;top:2544px">3</div>
<div class="step-text" style="left:640px;top:2285px">
  <h4>Once Login</h4>
  <p>Upload financial statements. Select preferences.<br>Finish the registration.</p>
</div>
<div class="step-text" style="left:702px;top:2418px">
  <h4>Automatic</h4>
  <p>Fare change We pick the cheapest fare for you and<br>carry out the change automatically.</p>
</div>
<div class="step-text" style="left:640px;top:2549px">
  <h4>Sit back and Save Money</h4>
  <p>Always switch automatically to the low fare.</p>
</div>
<div class="btn btn-cta">Register Now</div>

<footer class="site-footer">
  <div class="footer-brand">Sunvolt</div>
  <div class="footer-nav">That's How It Works | Prices | Ask? | About Us | Operations | Experience | Press</div>
  <div class="copyright">© Copyright 2019. All Rights Reserved.</div>
  <div class="social"></div>
</footer>

</body>
</html>
```